"Corporate Site Design of Cloud Application Venture"(Wordpress Design Project)

This task is new corporate site design for start-up.
Our company name is "Vantreel."
Vantreel is a cloud service for users who want to bring their software and settings on multiple computers.
Current beta service page is http://demo.vantreel-example.com . But, now it is not available.
We suggest sample sites below. But, we don't want to follow there. We need you to focus our logo and our company will serve stable service.
http://www.gallopix-example.com/design/481203/site-design-by-nortfield
http://www.gallopix-example.com/design/492715/site-design-by-qm
http://www.gallopix-example.com/design/470392
http://www.gallopix-example.com/design/418857
http://www.gallopix-example.com/design/409136
http://www.gallopix-example.com/design/413278
http://www.kintrabo-example.com/portfolio/plumvane/
http://tesselmarket-example.net/item/design-company-site/27415
http://www.orlivetstudio-example.com/images/corporate-dl-thumb.jpg
http://www.quorvenmart-example.com/product-tp/562093814/web_site_design_company.html
(1)we have already had logo-design and please must use it (attached).
we have attached 2 files.
Essential : vantreel.ai
voluntary : vantreelicon.ai
(2)Unfortunately, we have no idea now, so depend on you about color, lay-out and something, but we wish people feel deeply impressive when they get our website.
(3)Only if you want to use phrase of my service, please use “Where there is Vantreel, there’s your workspace.” (if the English grammar is not correct, please modify it.)
(4)The final design should look modern and sophisticated.
(5)Must have these contents.
In header.
- logo and facebook page link.(http://www.plinkhub-example.com/vantreel)
In Header Menu.
- Top Page (has several news release)
- "News Release" List and News Release Page
- "About Service"
- "About Us"
- "Contact"
And footter has several links.
ex. News release, about service, about us, contact, hiring and so on.

```html
<!DOCTYPE html>
<html lang="en">
<head>
<meta charset="utf-8">
<title>Vantreel — Cloud Workspace</title>
<link rel="stylesheet" href="https://fonts.googleapis.com/css2?family=Teko:wght@300;400;500&family=Arimo:wght@400&family=PT+Sans:wght@400&display=swap">
<style>
  :root{
    --navy:#0b3677;
    --navy-deep:#062d66;
    --rule:#1c3f74;
    --sky:#1e8fd2;
    --ink:#3d4246;
    --muted:#4f5559;
    --page:#d5dfe3;
    --page-light:#eef3f5;
    --btn-top:#f4f6f7;
    --btn-bottom:#d2d8dc;
  }
  *{margin:0;padding:0;box-sizing:border-box}
  html,body{width:1200px;height:979px;overflow:hidden}
  body{
    position:relative;
    background:
      radial-gradient(ellipse 420px 240px at 640px 250px,var(--page-light),transparent 70%),
      radial-gradient(ellipse 300px 120px at 260px 60px,#e6edf0,transparent 70%),
      var(--page);
    font-family:"Arimo",Arial,sans-serif;color:var(--ink);
  }
  .abs{position:absolute}
  .rule{position:absolute;left:141px;width:918px;height:2px;background:var(--rule)}

  /* header */
  .logo{left:160px;top:29px;font-family:"PT Sans",sans-serif;font-size:48px;color:var(--sky);letter-spacing:-1px;line-height:1}
  .social{top:13px;width:22px;height:22px;background:var(--navy);border:1px solid #fff}
  .search{left:919px;top:11px;width:140px;height:25px;border:2px solid var(--navy);background:#fff;display:flex}
  .search span{flex:1;font-size:13px;color:#556;padding:3px 6px;letter-spacing:.5px}
  .search i{width:27px;background:var(--navy);display:flex;align-items:center;justify-content:center}
  .nav a{position:absolute;top:67px;font-family:"Teko",sans-serif;font-weight:300;font-size:27px;color:var(--navy);text-decoration:none;letter-spacing:.5px;line-height:34px}
  .nav .current{left:569px;width:49px;height:34px;background:var(--navy);color:#fff;text-align:center}
  .nav .current::after{content:"";position:absolute;left:15px;top:34px;border:10px solid transparent;border-top:10px solid var(--navy);border-bottom:0}

  /* hero */
  .hero-title{left:175px;top:186px;font-family:"Teko",sans-serif;font-size:32px;line-height:35px;color:#222;font-weight:300;letter-spacing:.3px}
  .hero-title b{font-weight:500;color:var(--navy)}
  .hero-list{left:195px;top:268px;list-style:none;font-size:13.5px;line-height:21.5px;color:#444}
  .hero-list li::before{content:"";display:inline-block;width:5px;height:5px;border-radius:50%;background:#777;margin-right:9px;vertical-align:middle}
  .hero-art{left:487px;top:131px;width:544px;height:230px;border-radius:20px;
    background:radial-gradient(ellipse at 30% 40%,#f8fbfc,#dfe8ec 70%,transparent)}
  .dots{left:551px;top:401px;display:flex;gap:10px;align-items:center}
  .dots span{width:9px;height:9px;border-radius:50%;background:var(--navy);border:2px solid #9cc7ec}
  .dots .on{width:13px;height:13px;background:#fff;border:3px solid var(--navy)}

  /* read more */
  .more{position:absolute;width:118px;height:36px;display:flex;align-items:center;
    background:linear-gradient(var(--btn-top),var(--btn-bottom));
    box-shadow:0 6px 5px -4px rgba(0,0,0,.25);font-family:"PT Sans",sans-serif;font-size:17px;color:var(--navy)}
  .more svg{width:32px;height:36px;margin-right:5px;border-right:1px solid #bfc6ca}

  /* features */
  .feature{position:absolute;top:464px;width:282px}
  .feature h2{font-family:"Teko",sans-serif;font-weight:500;font-size:25px;line-height:23px;color:var(--navy)}
  .feature h2 span{display:block;font-weight:300}
  .feature .art{margin-top:7px;height:117px;background:linear-gradient(90deg,#0a3674,#0d3a7d 50%,#2a6bb8 85%,#0d3a7d)}
  .feature p{margin:11px 6px 0;font-size:12.6px;line-height:19.7px;color:var(--muted);letter-spacing:.2px}

  .intro{left:159px;top:795px;width:870px;font-size:12.5px;line-height:22.5px;color:var(--muted);letter-spacing:0}

  /* footer */
  .copy{left:155px;top:934px;font-family:"PT Sans",sans-serif;font-size:13px;color:var(--navy)}
  .foot-links{right:159px;top:934px;font-family:"PT Sans",sans-serif;font-size:13px;color:var(--navy);text-align:right;line-height:19px}
  .foot-links span{margin-left:14px}
</style>
</head>
<body>
  <div class="rule" style="top:10px"></div>
  <div class="abs logo">vantreel</div>

  <div class="abs social" style="left:870px" aria-label="Social link"></div>
  <div class="abs social" style="left:893px" aria-label="Social link"></div>
  <div class="abs search"><span>search...</span><i><svg width="14" height="14" viewBox="0 0 14 14"><circle cx="5.5" cy="5.5" r="4" fill="none" stroke="#fff" stroke-width="2"/><line x1="8.5" y1="8.5" x2="13" y2="13" stroke="#fff" stroke-width="2.5"/></svg></i></div>

  <nav class="nav">
    <a class="current" href="#">HOME</a>
    <a href="#" style="left:683px">ABOUT US</a>
    <a href="#" style="left:822px">NEWS RELEASE</a>
    <a href="#" style="left:993px">CONTACT</a>
  </nav>
  <div class="rule" style="top:100px"></div>

  <svg class="abs" style="left:150px;top:240px" width="17" height="34" viewBox="0 0 17 34"><path d="M15 1 L3 17 L15 33" fill="none" stroke="var(--navy)" stroke-width="3"/></svg>
  <svg class="abs" style="left:1034px;top:240px" width="17" height="34" viewBox="0 0 17 34"><path d="M2 1 L14 17 L2 33" fill="none" stroke="var(--navy)" stroke-width="3"/></svg>

  <h1 class="abs hero-title"><b>“ WHERE THERE IS</b> VANTREEL<br><b>&nbsp;&nbsp;&nbsp;THERE’S YOUR</b> WORKSPACE.”</h1>
  <ul class="abs hero-list">
    <li>Curabitur suscipt quam sed neque moiestie</li>
    <li>Nec suscipt ipsum hendrerit.</li>
    <li>Maecenas suscipt nulla in elit viverra vel</li>
    <li>vehicula nuc pellentesque.</li>
  </ul>
  <a class="more" style="left:208px;top:368px"><svg viewBox="0 0 32 36"><path d="M9 18a4 4 0 0 1 3-6 5 5 0 0 1 9 1 3 3 0 0 1 1 5z" fill="var(--navy)"/><path d="M16 17v8m-3-3 3 3 3-3" stroke="var(--navy)" stroke-width="2" fill="none"/></svg>Read more</a>

  <div class="abs hero-art" role="img" aria-label="Illustration of a globe, settings and cloud icons linked to a laptop and a cloud server cluster"></div>
  <div class="abs dots"><span></span><span></span><span class="on"></span><span></span><span></span></div>

  <div class="rule" style="top:438px"></div>

  <section class="feature" style="left:153px">
    <h2>BRING YOUR<span>APPS ANYWHERE</span></h2>
    <div class="art" role="img" aria-label="Database with download arrow beside a cloud and laptop"></div>
    <p>You can use your apps which you want on any computer anywhere.</p>
  </section>
  <section class="feature" style="left:462px">
    <h2>BRING YOUR<span>CONFIG ANYWHERE</span></h2>
    <div class="art" role="img" aria-label="Wrench and network cable beside a cloud and laptop"></div>
    <p>You can use your setting, add-ins and soon which you have been used on any computer anywhere.</p>
  </section>
  <section class="feature" style="left:768px">
    <h2>BRING YOUR<span>APPS FRIENDS</span></h2>
    <div class="art" role="img" aria-label="Group of user panels beside a cloud and gears"></div>
    <p>You can share your apps and settings including add-ins with your friends.</p>
  </section>

  <a class="more" style="left:313px;top:726px"><svg viewBox="0 0 32 36"><path d="M9 18a4 4 0 0 1 3-6 5 5 0 0 1 9 1 3 3 0 0 1 1 5z" fill="var(--navy)"/><path d="M16 17v8m-3-3 3 3 3-3" stroke="var(--navy)" stroke-width="2" fill="none"/></svg>Read more</a>
  <a class="more" style="left:624px;top:726px"><svg viewBox="0 0 32 36"><path d="M9 18a4 4 0 0 1 3-6 5 5 0 0 1 9 1 3 3 0 0 1 1 5z" fill="var(--navy)"/><path d="M16 17v8m-3-3 3 3 3-3" stroke="var(--navy)" stroke-width="2" fill="none"/></svg>Read more</a>
  <a class="more" style="left:929px;top:726px"><svg viewBox="0 0 32 36"><path d="M9 18a4 4 0 0 1 3-6 5 5 0 0 1 9 1 3 3 0 0 1 1 5z" fill="var(--navy)"/><path d="M16 17v8m-3-3 3 3 3-3" stroke="var(--navy)" stroke-width="2" fill="none"/></svg>Read more</a>

  <p class="abs intro">Lorem metus,&nbsp; volutpat orare molestie convallis, iaclis guis lectus. Ut varius risus eget neque tempus varius. Pellentesque sit amet m i vel quam dignis-sim convallis. Quisque elit quam, euismod nec convalis sed, lacils id est. Aloquam a lobirtis m i. Cras feugiat iaclis tellus, quis luctus nunc fermentum sit amet. Quisque lacina, lectus nec fermentum dictum.</p>

  <div class="rule" style="top:920px"></div>
  <footer>
    <div class="abs copy">Copyright © Vantreel Inc. - 2012.&nbsp; All Rights Reserved.</div>
    <div class="abs foot-links">
      <div><span>home</span><span>about us</span><span>contact us</span><span>hiring</span></div>
      <div>Blog | Testimonials | sitemap</div>
    </div>
  </footer>
</body>
</html>
```